Business Card Design

Cake decorating business in a small town in Australia. looking for a style that is fresh with a touch of vintage/country. liking these ideas, timber backgrounds, chalkboards, bunting, flowers and cake elements (rolling pins, cupcakes, cake stands, etc.) would consider a shot saying/statement. would like the back of the card to have wording "Specialising in delectable treats for all your special occasions" - wedding cakes - birthday cakes - special occasion cakes - novelty cakes - cupcakes, cookies, slices and cake pops. maybe incorporate a cake in design on back page. attached are a few of my favourite cakes and the start of a card design I liked.

Industry/Entity Type

Business

Contact Information for Business Card

Marigold's Sugarloft Bakes 0438 056 969Find me on (Chirpwall Logo)

Requirements
Nice to have
• timber, some of my designs, chalkboard, baking utensils
Should not have
• no red font

```html
<!DOCTYPE html>
<html lang="en">
<head>
<meta charset="utf-8">
<title>Marigold's Sugarloft Bakes – Business Card</title>
<link href="https://fonts.googleapis.com/css2?family=Dancing+Script:wght@500;700&display=swap" rel="stylesheet">
<style>
  :root {
    --backdrop: #ece7e4;
    --card-pink: #f8e9ed;
    --card-pink-light: #fcf3f5;
    --band-blue: #b3dde0;
    --ink-rose: #c06f86;
    --ink-deep: #9a5268;
    --badge-teal: #8fcfd2;
    --photo-cream: #d9c3a8;
    --photo-violet: #6f6bb0;
    --photo-cocoa: #9b7a62;
  }
  * { box-sizing: border-box; margin: 0; padding: 0; }
  html, body { width: 1200px; height: 801px; overflow: hidden; }
  body {
    background: var(--backdrop);
    display: flex;
    align-items: center;
    justify-content: center;
    gap: 40px;
    font-family: "Dancing Script", cursive;
    color: var(--ink-rose);
  }
  .card {
    position: relative;
    width: 540px;
    height: 309px;
    background: linear-gradient(180deg, var(--card-pink-light), var(--card-pink));
    box-shadow: 0 6px 18px rgba(80, 50, 60, .18);
    overflow: hidden;
  }
  .card__band {
    position: absolute;
    left: 0; right: 0;
    height: 14px;
    background: var(--band-blue);
  }
  .card__band--top { top: 0; }
  .card__band--bottom { bottom: 0; }

  /* Front face */
  .gallery {
    position: absolute;
    top: 48px; left: 34px;
    display: flex; gap: 12px;
  }
  .gallery__photo { width: 148px; height: 108px; border: 3px solid #fff; }
  .gallery__photo--cake { background: linear-gradient(135deg, var(--photo-cream), #a98f74); }
  .gallery__photo--novelty { background: linear-gradient(135deg, #8e8ad0, var(--photo-violet)); }
  .gallery__photo--stand { background: linear-gradient(135deg, #c7ad95, var(--photo-cocoa)); }
  .tagline {
    position: absolute;
    left: 34px; top: 180px;
    font-size: 30px;
    line-height: 1.15;
    font-weight: 700;
    color: var(--ink-rose);
  }

  /* Back face */
  .brand {
    position: absolute;
    top: 30px; left: 0; right: 0;
    display: flex; align-items: center; justify-content: center; gap: 14px;
  }
  .brand__dot { width: 44px; height: 44px; border-radius: 50%; background: var(--badge-teal); flex: none; }
  .brand__name { font-size: 32px; font-weight: 700; color: var(--ink-deep); white-space: nowrap; }
  .services {
    position: absolute;
    top: 92px; left: 60px; right: 60px;
    list-style: none;
    columns: 2;
    column-gap: 30px;
    font-size: 20px;
    line-height: 1.5;
    text-align: center;
    font-weight: 500;
  }
  .contact {
    position: absolute;
    bottom: 30px; left: 0; right: 0;
    display: flex; justify-content: center; gap: 34px;
    font-size: 19px; font-weight: 700;
    color: var(--ink-deep);
    white-space: nowrap;
  }
  .contact__item { display: flex; align-items: center; gap: 7px; }
  .contact__square { width: 14px; height: 14px; background: var(--ink-rose); }
</style>
</head>
<body>
  <section class="card card--front">
    <div class="card__band card__band--top"></div>
    <div class="gallery">
      <div class="gallery__photo gallery__photo--cake" role="img" aria-label="Photo of a decorated celebration cake"></div>
      <div class="gallery__photo gallery__photo--novelty" role="img" aria-label="Photo of a purple novelty cake"></div>
      <div class="gallery__photo gallery__photo--stand" role="img" aria-label="Photo of cupcakes on a cake stand"></div>
    </div>
    <p class="tagline">Specialising in delectable treats<br>for all your special occasions</p>
    <div class="card__band card__band--bottom"></div>
  </section>

  <section class="card card--back">
    <div class="card__band card__band--top"></div>
    <div class="brand">
      <span class="brand__dot"></span>
      <span class="brand__name">Marigold's Sugarloft Bakes</span>
    </div>
    <ul class="services">
      <li>Wedding Cakes</li>
      <li>Birthday Cakes</li>
      <li>Special Occasion Cakes</li>
      <li>Novelty Cakes</li>
      <li>Cupcakes</li>
      <li>Cookies</li>
      <li>Slices</li>
      <li>Cake Pops</li>
    </ul>
    <div class="contact">
      <span class="contact__item">
        <svg width="16" height="16" viewBox="0 0 24 24" aria-hidden="true"><path fill="#c06f86" d="M6.6 10.8a15 15 0 0 0 6.6 6.6l2.2-2.2a1 1 0 0 1 1-.25 11.4 11.4 0 0 0 3.6.57 1 1 0 0 1 1 1V20a1 1 0 0 1-1 1A17 17 0 0 1 3 4a1 1 0 0 1 1-1h3.5a1 1 0 0 1 1 1c0 1.25.2 2.45.57 3.6a1 1 0 0 1-.25 1z"/></svg>
        0417 382 254
      </span>
      <span class="contact__item">
        <span class="contact__square"></span>
        Chirpwall /Marigold's
      </span>
    </div>
    <div class="card__band card__band--bottom"></div>
  </section>
</body>
</html>
```